OzVoltix and TLW Alert insert/flyer

OzVoltix is an energy consulting firm which has been specializing in energy contract brokering, data management and consulting. We aim to bring value to our customers through open books communication and relevant information relating to their energy consumption. We have created a new patented design for an electricity consumption alert, which we send out monthly to clients. The alert example will be attached below which identifies a change in electricity consumption when compared to the previous month. We would like an advertisement to insert for the release of this insert. We work business to business trying to provide different saving opportunities for each client. We have a slogan currently in place “KEEP YOUR FINGER ON THE PULSE! – Stay aware and save money $$.” We would like to have the attached logos for both companies OzVoltix and TLW, and the contact box included on the insert. Please note, we require these inserts by 13th of november as we have a deadline. Please also find attached the patent number for the alert. Some content we would like to include is below;With the unique and patented energy usage alert system, any consumer connected to the electricity grid in QLD, NSW, ACT, VIC, SA, and TAS with a coms smart meter installed can have access to this system. This system is designed with both residential and commercial deployment in mind. A sample of commercial consumer that will benefit from this alert system but is not limited to:· Large Administrative Centres E.g. Head Office, Call Centres, etc.· Health Facilities – Hospitals – Aged Care Facilities, etc.· Educational Establishments: Universities, Colleges & Schools· Associations for Independent Retailers E.g. Independent supermarkets, Hardware stores· Hotels and Bottle Shops· Various hotel restaurants· Retail stores such as pharmacy store

Target Market(s)

Business in Australia.

Industry/Entity Type

Consulting

Font styles to use
Serif
Sans Serif

Colors

Designer to choose colors to be used in the design.

Requirements
Must have
• Must have OzVoltix and TLW logo, contact box and patent number.
Nice to have
• Alert images and icons, pictures that relate
• Some content we would like to include is below;
• With the unique and patented energy usage alert system, any consumer connected to the electricity grid in QLD, NSW, ACT, VIC, SA, and TAS with a coms smart meter installed can have access to this system. This system is designed with both residential and commercial deployment in mind. A sample of commercial consumer that will benefit from this alert system but is not limited to:
• · Large Administrative Centres E.g. Head Office, Call Centres, etc.
• · Health Facilities – Hospitals – Aged Care Facilities, etc.
• · Educational Establishments: Universities, Colleges & Schools
• · Associations for Independent Retailers E.g. Independent supermarkets, Hardware stores
• · Hotels and Bottle Shops
• · Various hotel restaurants
• · Retail stores such as pharmacy store
Should not have
• Images that have been copied/plagiarized,

```html
<!DOCTYPE html>
<html lang="en">
<head>
<meta charset="utf-8">
<title>OzVoltix – TLW Alert Flyer</title>
<link href="https://fonts.googleapis.com/css2?family=Montserrat:wght@400;500;600;700&family=Oswald:wght@600;700&display=swap" rel="stylesheet">
<style>
:root{
  --green:#2aa63a;
  --red:#c0151c;
  --orange:#f28a12;
  --ink:#2b2b2b;
  --panel:#ececec;
  --form:#f2f2f2;
  --footer:#262626;
  --icon:#f2c21b;
  --stage:#e9e6e2;
  --white:#ffffff;
}
*{box-sizing:border-box;margin:0;padding:0}
html,body{width:1200px;height:1200px;overflow:hidden;background:var(--stage);font-family:'Montserrat',sans-serif;color:var(--ink)}
.flyer{position:absolute;left:190px;top:20px;width:820px;height:1160px;background:var(--white);overflow:hidden;box-shadow:0 4px 18px rgba(0,0,0,.18)}

.hero-photo{position:absolute;left:0;top:130px;width:820px;height:270px;
  background:radial-gradient(ellipse 170px 130px at 370px 80px,#f6e27a 0%,#b89a2c 30%,rgba(60,60,60,0) 75%),linear-gradient(180deg,#2e2e2e,#3d3d3d 60%,#2a2a2a)}

.brand{position:absolute;left:36px;top:60px;display:flex;align-items:center;gap:8px}
.brand-dot{width:14px;height:14px;border-radius:50%;background:var(--green)}
.brand-name{font-weight:700;font-size:30px;color:var(--green);letter-spacing:.5px}

.headline{position:absolute;left:190px;top:34px;width:430px;text-align:center}
.headline-main{font-family:'Oswald',sans-serif;font-weight:700;font-size:29px;color:var(--green);letter-spacing:-.5px;line-height:1;white-space:nowrap}
.headline-sub{font-weight:700;font-size:19px;color:var(--red);margin-top:8px;white-space:nowrap}

.partner{position:absolute;right:0;top:0;width:190px;height:160px;background:var(--white);display:flex;flex-direction:column;align-items:center;justify-content:center;gap:2px}
.partner-row{display:flex;align-items:center;gap:8px}
.partner-square{width:14px;height:14px;background:var(--orange)}
.partner-name{font-weight:700;font-size:26px;color:var(--red)}
.partner-tag{font-size:14px;color:var(--red)}

.alert{position:absolute;left:420px;top:370px;width:400px;display:flex;flex-direction:column}
.alert-bar{background:var(--green);color:var(--white);font-weight:600;font-size:12px;padding:6px 16px}
.alert-panel{background:var(--panel);padding:12px 18px 14px 16px}
.alert-list{list-style:none}
.alert-list li{display:flex;gap:10px;font-size:11px;line-height:1.35;margin-bottom:4px}
.alert-list svg{flex:none;margin-top:2px}
.disclaimer{margin-top:12px;font-size:11px;line-height:1.4}
.disclaimer strong{color:var(--red);display:block}

.patent-top{height:14px;background:var(--green)}
.patent-box{background:var(--red);height:76px;position:relative;color:var(--white)}
.patent-label{position:absolute;left:18px;top:30px;font-weight:700;font-size:15px;line-height:1.1}
.patent-label span{display:block;color:var(--orange);font-weight:600;font-size:14px}
.patent-number{position:absolute;right:22px;top:14px;font-family:'Oswald',sans-serif;font-weight:700;font-size:36px}

.intro{position:absolute;left:30px;top:430px;width:370px;font-size:12px;line-height:1.5;text-align:justify}
.sectors{position:absolute;left:30px;top:592px;width:380px;list-style:none}
.sectors li{display:flex;align-items:center;gap:14px;font-size:12px;line-height:1.35;margin-bottom:10px}
.sector-icon{flex:none;width:30px;height:30px;border-radius:50%;background:var(--green);display:flex;align-items:center;justify-content:center}
.sector-icon i{display:block;width:12px;height:12px;background:var(--white);border-radius:2px}

.cta-bar{position:absolute;left:0;top:870px;width:820px;background:var(--green);color:var(--white);font-weight:600;font-size:14px;text-align:center;padding:7px}
.form{position:absolute;left:40px;top:918px;width:740px;background:var(--form);padding:10px 20px}
.form-row{display:flex;gap:30px;margin:8px 0}
.field{flex:1;display:flex;gap:8px;font-weight:700;font-size:12px}
.field-phone{flex:.6}
.field span{flex:1;border-bottom:1px dotted #555}
.send-note{position:absolute;left:40px;top:1038px;width:740px;font-size:14px;text-align:center}
.footer{position:absolute;left:0;bottom:0;width:820px;height:70px;background:var(--footer);color:var(--white);display:flex;align-items:center;justify-content:space-around;font-size:12px;padding:0 20px}
.contact{display:flex;align-items:center;gap:8px}
.contact svg{flex:none}
</style>
</head>
<body>
<main class="flyer">
  <div class="hero-photo" role="img" aria-label="Woman looking up at a glowing light bulb drawn on a chalkboard with hanging chalk bulbs"></div>

  <div class="brand"><span class="brand-dot"></span><span class="brand-name">OzVoltix</span></div>

  <header class="headline">
    <h1 class="headline-main">KEEP YOUR FINGER ON THE PULSE!</h1>
    <p class="headline-sub">Stay aware and save money $$</p>
  </header>

  <div class="partner">
    <div class="partner-row"><span class="partner-square"></span><span class="partner-name">TLW</span></div>
    <span class="partner-tag">Metering Data</span>
  </div>

  <section class="alert">
    <div class="alert-bar">Electricity Alert for your site at:</div>
    <div class="alert-panel">
      <ul class="alert-list">
        <li><svg width="12" height="12" viewBox="0 0 12 12"><circle cx="6" cy="6" r="6" fill="#f28a12"/><path d="M3 6.2l2 2 4-4" stroke="#fff" stroke-width="1.6" fill="none"/></svg>You have reached 60% of your monthly Peak target electricity consumption.</li>
        <li><svg width="12" height="12" viewBox="0 0 12 12"><circle cx="6" cy="6" r="6" fill="#f28a12"/><path d="M3 6.2l2 2 4-4" stroke="#fff" stroke-width="1.6" fill="none"/></svg>This was reached on the 11/11/2018.</li>
        <li><svg width="12" height="12" viewBox="0 0 12 12"><circle cx="6" cy="6" r="6" fill="#f28a12"/><path d="M3 6.2l2 2 4-4" stroke="#fff" stroke-width="1.6" fill="none"/></svg>You reached this target in 11 days.</li>
        <li><svg width="12" height="12" viewBox="0 0 12 12"><circle cx="6" cy="6" r="6" fill="#f28a12"/><path d="M3 6.2l2 2 4-4" stroke="#fff" stroke-width="1.6" fill="none"/></svg>Your target electricity consumption is based on your previous months usage.</li>
        <li><svg width="12" height="12" viewBox="0 0 12 12"><circle cx="6" cy="6" r="6" fill="#f28a12"/><path d="M3 6.2l2 2 4-4" stroke="#fff" stroke-width="1.6" fill="none"/></svg>Total volume of Peak 1 714.12 kWh</li>
        <li><svg width="12" height="12" viewBox="0 0 12 12"><circle cx="6" cy="6" r="6" fill="#f28a12"/><path d="M3 6.2l2 2 4-4" stroke="#fff" stroke-width="1.6" fill="none"/></svg>Total volume of Off Peak 3 195.31 kWh</li>
        <li><svg width="12" height="12" viewBox="0 0 12 12"><circle cx="6" cy="6" r="6" fill="#f28a12"/><path d="M3 6.2l2 2 4-4" stroke="#fff" stroke-width="1.6" fill="none"/></svg>Total volume of Shoulder 0.00 kWh</li>
        <li><svg width="12" height="12" viewBox="0 0 12 12"><circle cx="6" cy="6" r="6" fill="#f28a12"/><path d="M3 6.2l2 2 4-4" stroke="#fff" stroke-width="1.6" fill="none"/></svg>Your consumption has increased by 100.67% from last month.</li>
        <li><svg width="12" height="12" viewBox="0 0 12 12"><circle cx="6" cy="6" r="6" fill="#f28a12"/><path d="M3 6.2l2 2 4-4" stroke="#fff" stroke-width="1.6" fill="none"/></svg>Figures based on usage from 01/11/2018 - 11/11/2018</li>
        <li><svg width="12" height="12" viewBox="0 0 12 12"><circle cx="6" cy="6" r="6" fill="#f28a12"/><path d="M3 6.2l2 2 4-4" stroke="#fff" stroke-width="1.6" fill="none"/></svg>If you have any questions about this Alert, please don't hesitate to contact OzVoltix.</li>
      </ul>
      <p class="disclaimer"><strong>Disclaimer:</strong>Please note that variation can occur as all files arrived have a national average of up to 15% in Error Code. Additionally, this message may lag by 24 - 48 hours.</p>
    </div>
    <div class="patent">
      <div class="patent-top"></div>
      <div class="patent-box">
        <p class="patent-label">PATENT NUMBER<span>for the alert</span></p>
        <p class="patent-number">2013105517</p>
      </div>
    </div>
  </section>

  <p class="intro">With the unique and patented energy usage alert system, any consumer connected to the electricity grid in QLD, NSW, ACT, VIC, SA, and TAS with a coms smart meter installed can have access to this system. This system is designed with both residential and commercial deployment in mind. A sample of commercial consumer that will benefit from this alert system but is not limited to:</p>

  <ul class="sectors">
    <li><span class="sector-icon"><i></i></span><span>Large Administrative Centres E.g. Head Office, Call Centres, etc.</span></li>
    <li><span class="sector-icon"><i></i></span><span><strong>Health Facilities</strong> – Hospitals – Aged Care Facilities, etc.</span></li>
    <li><span class="sector-icon"><i></i></span><span><strong>Educational Establishments:</strong> Universities, Colleges &amp; Schools</span></li>
    <li><span class="sector-icon"><i></i></span><span>Associations for Independent Retailers E.g. Independent supermarkets, Hardware stores</span></li>
    <li><span class="sector-icon"><i></i></span><span>Hotels and Bottle Shops</span></li>
    <li><span class="sector-icon"><i></i></span><span>Various hotel restaurants</span></li>
    <li><span class="sector-icon"><i></i></span><span>Retail stores such as pharmacy store</span></li>
  </ul>

  <div class="cta-bar">Get your complimentary electricity review today!</div>
  <form class="form">
    <div class="form-row"><label class="field">Name:<span></span></label><label class="field field-phone">Phone:<span></span></label></div>
    <div class="form-row"><label class="field">Email:<span></span></label></div>
    <div class="form-row"><label class="field">Address:<span></span></label></div>
  </form>
  <p class="send-note">SMS, fax or email this completed form along with a recent energy bill, &amp; we'll get back to you ASAP!</p>

  <footer class="footer">
    <span class="contact"><svg width="16" height="16" viewBox="0 0 16 16"><path d="M3 1l3 3-2 2c1 2 3 4 5 5l2-2 3 3-2 2C7 14 2 9 1 3z" fill="#f2c21b"/></svg>1300 555 018</span>
    <span class="contact"><svg width="16" height="14" viewBox="0 0 16 14"><rect x="1" y="1" width="14" height="9" rx="1" fill="none" stroke="#f2c21b" stroke-width="1.5"/><path d="M4 10v3l3-3" fill="#f2c21b"/></svg>0400 555 217</span>
    <span class="contact"><svg width="16" height="14" viewBox="0 0 16 14"><rect x="1" y="5" width="14" height="7" fill="#f2c21b"/><rect x="4" y="1" width="8" height="4" fill="#f2c21b"/></svg>(03) 5550 1234</span>
    <span class="contact"><svg width="16" height="12" viewBox="0 0 16 12"><rect x="0" y="0" width="16" height="12" fill="#f2c21b"/><path d="M0 0l8 6 8-6" stroke="#262626" fill="none"/></svg>contactus@ozvoltix.com</span>
    <span class="contact"><svg width="14" height="14" viewBox="0 0 14 14"><circle cx="7" cy="7" r="6" fill="none" stroke="#f2c21b" stroke-width="1.5"/><path d="M1 7h12M7 1v12" stroke="#f2c21b"/></svg>www.ozvoltix.com</span>
  </footer>
</main>
</body>
</html>
```